World Class Resort Requires Design for Marketing and Large Road Signage Purposes

We want a design that will take us to a new level, you can visit our web address to see the property details, www.corbenmeadow.com we want the design to be full of colour, character, and a real one off it must attract customers including children to visit our resort / adventure park. we require the following features etc in the design by way of design not words - Golf Course - Mini Golf 18 holes - Jumping Pillow - Pedal Bikes - Water Bubbles - Lakeside Dining - Resort Accommodation - Swiss Shopping Village - Ice Cream Shop - Bakery - Wedding Chapel - Conferences - Hillside Look out - Numerous Lakes with Ducks trees and trout fish - Mountain Streams - Lakeside Villas.

The resort is built around a Swiss style theme buildings and is located in one of the most exotic - green, leafy, grassy areas of the World - The main design focus is to be on FELSKORNBERG.COM.AU , the design must say 10 minutes drive North of Launceston

The design will be used on large 6 metre - 4 metre billboards around the State of Tasmania Australia
Updates

Hello,  We have just posted a number of images of the property and its features - we would like to follow the animated type Pemberly theme or similar as also posted on the brief  Please advise if you need anything extra  Thanks Rod  ROD@KQ.COM.AU

The uploaded file number 4 of Pemberly Park is the similar theme we would like created = all other images posted are of our property features Thanks Rod

Reason: Date has been extended as designer have requested some extra time to submit their designs Thanks

Reason: Designers have asked for additional time

Target Market(s)

Families, Weddings, Conferences, Holiday Makers, Day Visitors - Please look at the image we have uploaded as a similar format if possible. Thanks Rod

Industry/Entity Type

Accommodation

Font styles to use
Decorative

Requirements
Must have
• we require the following features etc in the design by way of design not words - Golf Course - Mini Golf 18 holes - Jumping Pillow - Pedal Bikes - Water Bubbles - Lakeside Dining - Resort Accommodation - Swiss Shopping Village - Ice Cream Shop - Bakery - Wedding Chapel - Conferences - Hillside Look out - Numerous Lakes with Ducks trees and trout fish - Mountain Streams - Lakeside Villas.
Must have an exotic - green, leafy, Hillside stream, lake, grassy appeal and be fun and exciting as well
The main design focus is to be on FELSKORNBERG.COM.AU , the design must say 10 minutes drive North of Launceston
Should not have
• Dark Colours, dreary design, to much text

```html
<!DOCTYPE html>
<html lang="en">
<head>
<meta charset="utf-8">
<title>Corben Meadow – Billboard</title>
<link rel="stylesheet" href="https://fonts.googleapis.com/css2?family=Archivo+Black&family=Arimo:wght@400;700&display=swap">
<style>
  :root {
    --page-bg: #2a2d2b;
    --green-deep: #0d7a26;
    --green-mid: #2fa63a;
    --green-light: #7fd04a;
    --cream: #f4f1e4;
    --cream-shade: #d9d6c6;
    --ring: #1c6a2c;
    --ink: #151515;
    --white: #ffffff;
  }
  html, body {
    margin: 0;
    width: 1200px;
    height: 800px;
    overflow: hidden;
    background: var(--page-bg);
  }
  .canvas {
    position: relative;
    width: 1200px;
    height: 800px;
  }
  .billboard {
    position: absolute;
    left: 40px;
    top: 150px;
    width: 1120px;
    height: 500px;
    overflow: hidden;
  }
  .billboard-art {
    position: absolute;
    inset: 0;
    width: 1120px;
    height: 500px;
  }
  .tagline {
    position: absolute;
    left: 70px;
    top: 352px;
    margin: 0;
    color: var(--ink);
    font-family: "Arimo", Arial, sans-serif;
    font-weight: 400;
    font-size: 46px;
    line-height: 60px;
    letter-spacing: 0.5px;
  }
  .tagline strong {
    font-family: "Archivo Black", "Arial Black", sans-serif;
    font-weight: 400;
  }
  .brand {
    position: absolute;
    right: 28px;
    top: 52px;
    text-align: right;
    color: var(--white);
  }
  .brand-name {
    margin: 0;
    font-family: "Archivo Black", "Arial Black", sans-serif;
    font-size: 50px;
    line-height: 56px;
    letter-spacing: 1px;
  }
  .brand-url {
    margin: 4px 0 0;
    font-family: "Arimo", Arial, sans-serif;
    font-size: 17px;
  }
</style>
</head>
<body>
<main class="canvas">
  <section class="billboard" aria-label="Corben Meadow roadside billboard">
    <svg class="billboard-art" viewBox="0 0 1120 500" xmlns="http://www.w3.org/2000/svg">
      <defs>
        <linearGradient id="board-green" x1="0" y1="0" x2="1" y2="1">
          <stop offset="0" stop-color="var(--green-deep)"/>
          <stop offset="0.6" stop-color="var(--green-mid)"/>
          <stop offset="1" stop-color="var(--green-deep)"/>
        </linearGradient>
        <radialGradient id="cream-glow" cx="0.35" cy="0.3" r="0.8">
          <stop offset="0" stop-color="var(--white)"/>
          <stop offset="0.7" stop-color="var(--cream)"/>
          <stop offset="1" stop-color="var(--cream-shade)"/>
        </radialGradient>
        <linearGradient id="band-green" x1="0" y1="0" x2="0" y2="1">
          <stop offset="0" stop-color="var(--green-light)"/>
          <stop offset="0.35" stop-color="var(--green-mid)"/>
          <stop offset="1" stop-color="var(--green-deep)"/>
        </linearGradient>
        <linearGradient id="photo-golf" x1="0" y1="0" x2="0" y2="1">
          <stop offset="0" stop-color="#9cc86a"/><stop offset="1" stop-color="#3f7f2a"/>
        </linearGradient>
        <linearGradient id="photo-bridge" x1="0" y1="0" x2="0" y2="1">
          <stop offset="0" stop-color="#7fae5a"/><stop offset="0.55" stop-color="#4f7f36"/><stop offset="1" stop-color="#2f5a3c"/>
        </linearGradient>
        <linearGradient id="photo-pillow" x1="0" y1="0" x2="0" y2="1">
          <stop offset="0" stop-color="#b9cde6"/><stop offset="0.55" stop-color="#7aa356"/><stop offset="1" stop-color="#c9a26a"/>
        </linearGradient>
        <linearGradient id="photo-bubble" x1="0" y1="0" x2="0" y2="1">
          <stop offset="0" stop-color="#6d8fa2"/><stop offset="0.5" stop-color="#c2344a"/><stop offset="1" stop-color="#5a7f8e"/>
        </linearGradient>
        <linearGradient id="photo-village" x1="0" y1="0" x2="0" y2="1">
          <stop offset="0" stop-color="#9ab9d6"/><stop offset="0.45" stop-color="#b86a45"/><stop offset="1" stop-color="#4f8a34"/>
        </linearGradient>
      </defs>

      <rect class="board-base" width="1120" height="500" fill="url(#board-green)"/>
      <path class="cream-swoosh" fill="url(#cream-glow)"
        d="M0,0 H700 C830,150 935,330 1005,500 H720 C650,420 560,335 360,322 C220,314 90,320 0,332 Z"/>
      <path class="tagline-band" fill="url(#band-green)"
        d="M0,318 C120,300 260,296 380,306 C560,322 660,420 720,500 H0 Z"/>

      <g class="feature-photo" role="img" aria-label="Golf ball on tee in green grass">
        <ellipse cx="80" cy="238" rx="105" ry="68" fill="url(#photo-golf)" stroke="var(--ring)" stroke-width="6"/>
      </g>
      <g class="feature-photo" role="img" aria-label="Wooden footbridge over a lake among trees">
        <ellipse cx="310" cy="205" rx="112" ry="82" fill="url(#photo-bridge)" stroke="var(--ring)" stroke-width="6"/>
      </g>
      <g class="feature-photo" role="img" aria-label="Colourful jumping pillow on a lawn under blue sky">
        <ellipse cx="542" cy="195" rx="104" ry="80" fill="url(#photo-pillow)" stroke="var(--ring)" stroke-width="6"/>
      </g>
      <g class="feature-photo" role="img" aria-label="Red water bubble ride on the lake">
        <ellipse cx="752" cy="295" rx="90" ry="82" fill="url(#photo-bubble)" stroke="var(--ring)" stroke-width="6"/>
      </g>
      <g class="feature-photo" role="img" aria-label="Swiss style village buildings and mini golf">
        <ellipse cx="908" cy="418" rx="94" ry="86" fill="url(#photo-village)" stroke="var(--ring)" stroke-width="6"/>
      </g>
    </svg>

    <p class="tagline">
      <strong>10 MINUTES</strong> DRIVE<br>
      NORTH OF <strong>LAUNCESTON</strong>
    </p>

    <div class="brand">
      <p class="brand-name">LOGO</p>
      <p class="brand-url">www.corbenmeadow.com</p>
    </div>
  </section>
</main>
</body>
</html>
```